Packing for Disinfectant wipes

Design the Packinging for new Disinfectant wipes. Wipes are for cleaning and disinfectanting hard surfaces and equipment. There are 100 wipes to the packet (size 230mm x 300mm). The company is called Norbeck Supplies and is supplier of consumable products to healthcare companies. Wipes are not for use on humans/baby. Packaging size as per attachment.
Industry/Entity Type
Healthcare
Requirements
Nice to have
- Packaging need ingredients list and directions for use

```html
<!DOCTYPE html>
<html lang="en">
<head>
<meta charset="utf-8">
<title>Norbeck Supplies – Disinfectant Wipes Packaging</title>
<link href="https://fonts.googleapis.com/css2?family=Montserrat:wght@400;500;600;700&display=swap" rel="stylesheet">
<style>
  :root{
    --ink:#3d4a55;
    --green:#8dc63f;
    --green-deep:#39b54a;
    --lime:#d7df23;
    --blue:#29abe2;
    --blue-deep:#0b6fb8;
    --blue-pale:#a6d1ec;
    --orange:#f7941d;
    --peach:#fdc97a;
    --rule:#d3d3d3;
    --paper:#ffffff;
  }
  *{margin:0;padding:0;box-sizing:border-box}
  html,body{width:670px;height:1200px;overflow:hidden;background:var(--paper)}
  body{font-family:'Montserrat',sans-serif;color:var(--ink);position:relative}
  .abs{position:absolute}

  .crop{position:absolute;background:var(--rule)}
  .crop.v{width:1px;height:20px}
  .crop.h{height:1px;width:20px}

  .dieline{position:absolute;left:65px;top:71px;width:529px;height:1011px;border:1px solid var(--rule)}
  .fold{position:absolute;left:65px;width:529px;height:1px;background:var(--rule)}

  .info{font-size:7.2px;font-weight:600;line-height:11.2px;letter-spacing:.1px}
  .info p{white-space:nowrap}
  .gap{margin-top:4px}

  .brand{font-weight:600;color:var(--ink);display:flex;align-items:center;gap:4px;white-space:nowrap}
  .brand .mark{background:var(--green);display:inline-block}

  .badge-plain{border-radius:50%;background:var(--green)}

  .upside{transform:rotate(180deg);transform-origin:center}
  .banner{background:linear-gradient(90deg,var(--green),#c3d82e);clip-path:polygon(0 0,100% 4%,100% 100%,0 96%);
    color:#fff;font-size:6.2px;line-height:7px;padding:10px 16px 0 18px;font-weight:500}

  .mosaic{left:66px;top:394px;width:528px;height:191px;
    background:linear-gradient(90deg,#a9cf45 0%,#3f93d1 14%,#8fcbed 26%,#f7941d 38%,#8dc63f 52%,#39b54a 60%,#c6dc3a 70%,#f7a23a 76%,#9fd0ee 86%,#0b6fb8 100%)}

  .title-a{font-weight:700;color:var(--ink);text-align:right;white-space:nowrap}
  .title-b{font-weight:700;color:var(--green);text-align:right;white-space:nowrap}
  .count{background:linear-gradient(160deg,#a4cd3a,var(--green));clip-path:polygon(0 6%,100% 0,100% 94%,0 100%);
    color:#fff;text-align:center;font-weight:600;line-height:1}
  .count .n{display:block}
  .count .w{display:block}
  .count .s{display:block}

  .band{color:#fff;font-weight:700;text-align:center;letter-spacing:.4px;font-size:13px;line-height:26px}
  .band.dir{background:linear-gradient(90deg,var(--blue),#8bd3f3);clip-path:polygon(0 4%,100% 0,100% 96%,0 100%)}
  .band.ing{background:linear-gradient(90deg,var(--orange),#f9ae44);clip-path:polygon(0 0,100% 4%,100% 100%,0 96%)}

  .step-art{background:#e7ebee;border-radius:6px}
  .step-cap{font-size:6.2px;font-weight:700;text-align:center;line-height:6.4px}
  .ing-text{font-size:6.2px;line-height:5.9px;text-align:justify;text-align-last:left;font-weight:400}
</style>
</head>
<body>

<!-- crop marks -->
<div class="crop v" style="left:65px;top:46px"></div>
<div class="crop v" style="left:594px;top:46px"></div>
<div class="crop v" style="left:65px;top:1090px"></div>
<div class="crop v" style="left:594px;top:1090px"></div>
<div class="crop h" style="left:40px;top:71px"></div>
<div class="crop h" style="left:600px;top:71px"></div>
<div class="crop h" style="left:40px;top:1082px"></div>
<div class="crop h" style="left:600px;top:1082px"></div>

<div class="dieline"></div>
<div class="fold" style="top:255px"></div>
<div class="fold" style="top:393px"></div>
<div class="fold" style="top:761px"></div>
<div class="fold" style="top:898px"></div>

<!-- Panel 1: information -->
<div class="abs info" style="left:124px;top:102px">
  <p>Marketed by :</p>
  <p>Norbeck Supplies local adress lorem ipsum</p>
  <p>Plot No 14, Riverside 38</p>
  <p>Customer care N0: 90412 66718</p>
  <p>Email: support@norbecksupplies.com</p>
  <p>Follo us for information, product launches and</p>
  <p>details on facebook: @Norbecksupplies</p>
</div>
<div class="abs brand" style="left:214px;top:200px;font-size:12px">
  <span class="mark" style="width:8px;height:8px"></span>Norbeck Supplies
</div>

<div class="abs info" style="left:362px;top:102px">
  <p>Net Content : 100 wipes</p>
  <p>Wipe size:230mmx300mm</p>
  <p>Best before : 24 months from manifacturer</p>
  <p class="gap">B.NO. / Mfg. Date:</p>
  <p>M.R.P. : ()*</p>
  <p>(Inclusive of all taxes)</p>
</div>
<div class="abs badge-plain" style="left:461px;top:186px;width:18px;height:18px"></div>
<div class="abs badge-plain" style="left:461px;top:209px;width:18px;height:18px"></div>

<!-- Panel 2: top flap (upside down) -->
<div class="abs upside" style="left:156px;top:283px;width:340px;height:81px">
  <div class="abs brand" style="left:0;top:8px;font-size:15px;flex-direction:column;align-items:flex-start;gap:0;line-height:16px">
    <span style="display:flex;align-items:center;gap:4px"><span class="mark" style="width:9px;height:9px"></span>Norbeck</span>
    <span style="color:var(--green);font-size:14px;padding-left:13px">wipes</span>
  </div>
  <div class="abs banner" style="left:106px;top:10px;width:234px;height:56px">
    Norbeck wipes are the perfect solutions for Lorem ipsum dolor sit amet, consectetuer adipiscing elit, sed diam nonummy nibh euismod tincidunt ut laoreet dolore magna aliquam erat volutpat. Ut wisi enim ad minim veniam, quis nostrud exerci tation ullamcorper suscipit lobortis nisl ut .
  </div>
</div>

<!-- Panel 3: front -->
<div class="abs mosaic" role="img" aria-label="Decorative band of overlapping coloured brand panels in green, blue and orange"></div>

<svg class="abs" style="left:210px;top:519px" width="254" height="123" viewBox="0 0 254 123" aria-hidden="true">
  <path d="M18 1 H210 C232 1 252 22 252 46 V52 C252 62 246 70 236 74 C216 82 208 94 204 108 C200 118 192 121 182 121 H18 C9 121 1 114 1 104 V18 C1 9 9 1 18 1 Z"
        fill="none" stroke="#cfcfcf" stroke-width=".8"/>
</svg>

<div class="abs brand" style="left:258px;top:652px;font-size:20px">
  <span class="mark" style="width:12px;height:12px"></span>Norbeck Supplies
</div>

<div class="abs title-a" style="right:398px;top:706px;font-size:17.5px">Disinfectant</div>
<div class="abs title-b" style="right:398px;top:725px;font-size:17.5px">Wipes</div>
<div class="abs count" style="left:280px;top:702px;width:32px;height:47px;padding-top:7px">
  <span class="n" style="font-size:17px;letter-spacing:-1px">100</span>
  <span class="w" style="font-size:8px;margin-top:1px">WIPES</span>
  <span class="s" style="font-size:2.6px;margin-top:2px">230mm x 300mm</span>
</div>
<div class="abs title-a" style="right:174px;top:707px;font-size:13.5px">All Purpose anti-bacterial</div>
<div class="abs title-b" style="right:174px;top:721px;font-size:22px">cleaning wipes</div>

<!-- Panel 4: side -->
<div class="abs title-a" style="right:432px;top:816px;font-size:12px">Disinfectant</div>
<div class="abs title-b" style="right:432px;top:828px;font-size:12px">Wipes</div>
<div class="abs count" style="left:244px;top:812px;width:23px;height:34px;padding-top:5px">
  <span class="n" style="font-size:12px;letter-spacing:-.8px">100</span>
  <span class="w" style="font-size:5.6px;margin-top:1px">WIPES</span>
  <span class="s" style="font-size:2px;margin-top:1px">230mm x 300mm</span>
</div>
<div class="abs title-a" style="right:272px;top:818px;font-size:9.5px">All Purpose anti-bacterial</div>
<div class="abs title-b" style="right:272px;top:827px;font-size:15px">cleaning wipes</div>
<div class="abs brand" style="left:408px;top:822px;font-size:13px">
  <span class="mark" style="width:9px;height:9px"></span>Norbeck Supplies
</div>

<!-- Panel 5: directions & ingredients -->
<div class="abs band dir" style="left:121px;top:952px;width:195px;height:26px">DIRECTIONS FOR USE</div>
<div class="abs band ing" style="left:347px;top:952px;width:196px;height:26px">INGREDIENTS</div>

<div class="abs step-art" style="left:127px;top:986px;width:44px;height:31px" role="img" aria-label="Line drawing of a hand peeling open the sticker"></div>
<div class="abs step-art" style="left:197px;top:986px;width:44px;height:31px" role="img" aria-label="Line drawing of a hand pulling a wipe from the pack"></div>
<div class="abs step-art" style="left:260px;top:986px;width:44px;height:31px" role="img" aria-label="Line drawing of the pack with the resealable flap closing"></div>

<div class="abs step-cap" style="left:116px;top:1021px;width:72px">Open the sticker releasable</div>
<div class="abs step-cap" style="left:192px;top:1021px;width:54px">Use wipes as required</div>
<div class="abs step-cap" style="left:247px;top:1021px;width:72px">Close the resealable flap property after use</div>

<div class="abs ing-text" style="left:347px;top:989px;width:195px">
  Lorem ipsum dolor sit amet, consectetuer adipiscing elit, sed diam nonummy nibh euismod tincidunt ut laoreet dolore magna aliquam erat volutpat. Ut wisi enim ad minim veniam, quis nostrud exerci tation ullamcorper suscipit lobortis nisl ut aliquip ex ea commodo consequat. Duis autem vel eum iriure dolor in hendrerit in vulputate velit esse molestie consequat, vel illum dolore eu feugiat nulla facilisis at vero eros et accum-san et iusto odio
</div>

</body>
</html>
```